KWM Plumbing and Roofing

design a fresh modern card for a young plumbing business looking to break into the market.
Must include the logo in the attached file
Lowen Fairbrook
Phone number 0412689405
Vic Licence no 63920
email......

New Homes & Renovations
General Plumbing & Maintenance
Solar Hot Water Units
Roofing & Guttering (new and replacement)

Industry/Entity Type

Business

```html
<!DOCTYPE html>
<html lang="en">
<head>
<meta charset="utf-8">
<title>KWM Plumbing and Roofing – Business Card</title>
<link rel="stylesheet" href="https://fonts.googleapis.com/css2?family=Fira+Sans:ital,wght@0,600;0,700;1,700&display=swap">
<style>
  :root {
    --backdrop: #ece7e0;
    --card: #ffffff;
    --navy: #0d4672;
    --deep: #0a3a60;
    --teal: #1f86ad;
    --ink: #123c6b;
    --gold: #d19a36;
  }
  * { margin: 0; padding: 0; box-sizing: border-box; }
  html, body { width: 1200px; height: 1000px; overflow: hidden; }
  body {
    background: var(--backdrop);
    font-family: "Fira Sans", Arial, sans-serif;
    position: relative;
  }
  .card {
    position: absolute;
    left: 340px;
    width: 540px;
    height: 344px;
    background: var(--card);
    overflow: hidden;
    box-shadow: 0 4px 10px rgba(0,0,0,0.25);
  }
  .card--front { top: 131px; }
  .card--back { top: 526px; }
  .card__swoosh { position: absolute; inset: 0; width: 100%; height: 100%; }

  .brand {
    position: absolute;
    display: flex;
    align-items: center;
    color: var(--navy);
    font-weight: 700;
  }
  .brand__dot { border-radius: 50%; background: var(--navy); flex: none; }
  .card--front .brand { left: 104px; top: 128px; gap: 16px; }
  .card--front .brand__dot { width: 84px; height: 84px; }
  .card--front .brand__name { font-size: 25px; line-height: 1.15; }

  .card--back .brand {
    left: 36px; top: 42px;
    flex-direction: column; gap: 8px; width: 86px; text-align: center;
  }
  .card--back .brand__dot { width: 60px; height: 60px; }
  .card--back .brand__name { font-size: 10px; line-height: 1.2; }

  .contact {
    position: absolute;
    left: 136px; top: 44px;
    list-style: none;
    color: var(--ink);
    font-weight: 600;
    font-size: 14px;
    line-height: 26.5px;
  }
  .contact__name { text-transform: uppercase; letter-spacing: 0.3px; }

  .services {
    position: absolute;
    left: 198px; top: 198px;
    list-style: none;
    color: var(--ink);
    font-weight: 700;
    font-style: italic;
    font-size: 14px;
    line-height: 26.5px;
  }
  .services li { display: flex; align-items: center; gap: 5px; }
  .services li::before {
    content: "";
    width: 4px; height: 4px;
    border-radius: 50%;
    background: var(--gold);
    flex: none;
  }
</style>
</head>
<body>

<section class="card card--front" aria-label="Card front">
  <svg class="card__swoosh" viewBox="0 0 540 344" aria-hidden="true">
    <defs>
      <linearGradient id="bandFront" x1="0" y1="0" x2="1" y2="1">
        <stop offset="0" stop-color="var(--deep)"/>
        <stop offset="0.6" stop-color="var(--teal)"/>
        <stop offset="1" stop-color="var(--navy)"/>
      </linearGradient>
    </defs>
    <path d="M0,0 H215 C130,25 45,80 0,150 Z" fill="url(#bandFront)"/>
    <path d="M0,150 C45,80 130,25 215,0 H200 C120,28 40,78 0,138 Z" fill="var(--teal)" opacity="0.6"/>
    <path d="M540,198 C470,288 380,330 290,344 H540 Z" fill="url(#bandFront)"/>
    <path d="M540,198 C470,288 380,330 290,344 H305 C392,328 478,290 540,212 Z" fill="var(--teal)" opacity="0.6"/>
  </svg>
  <div class="brand">
    <span class="brand__dot"></span>
    <span class="brand__name">KWM Plumbing and Roofing</span>
  </div>
</section>

<section class="card card--back" aria-label="Card back">
  <svg class="card__swoosh" viewBox="0 0 540 344" aria-hidden="true">
    <defs>
      <linearGradient id="bandBack" x1="1" y1="0" x2="0" y2="1">
        <stop offset="0" stop-color="var(--deep)"/>
        <stop offset="0.6" stop-color="var(--teal)"/>
        <stop offset="1" stop-color="var(--navy)"/>
      </linearGradient>
    </defs>
    <path d="M320,0 C415,15 500,65 540,140 V0 Z" fill="url(#bandBack)"/>
    <path d="M320,0 C415,15 500,65 540,140 V126 C495,58 410,12 338,0 Z" fill="var(--teal)" opacity="0.6"/>
    <path d="M0,200 C50,290 150,336 265,344 H0 Z" fill="url(#bandBack)"/>
    <path d="M0,200 C50,290 150,336 265,344 H245 C140,332 45,285 0,216 Z" fill="var(--teal)" opacity="0.6"/>
  </svg>
  <div class="brand">
    <span class="brand__dot"></span>
    <span class="brand__name">KWM Plumbing and Roofing</span>
  </div>
  <ul class="contact">
    <li class="contact__name">Lowen Fairbrook</li>
    <li>Tel: 0412689405</li>
    <li>Vic Licence No. 63920</li>
    <li>email: mail@kwmplumbing.example</li>
  </ul>
  <ul class="services">
    <li>New Homes &amp; Renovations</li>
    <li>General Plumbing &amp; Maintenance</li>
    <li>Solar Hot Water Units</li>
    <li>Roofing &amp; Guttering (new and replacement)</li>
  </ul>
</section>

</body>
</html>
```